To design the Curriculum Vitae of a General Manager Legal

the objective is to redesign the attached Résumé for a senior level Internal Legal Executive in order to make it attractive, easily readable, catchy, modern looking while staying classy, elegant, sobre, and serious.
The résumé is attached to this project. it contains the followings sections : Photo; Contact Details; Summary; Education; Experience; Other.
Feel free to use photoshop to improve photo.
Updates

Target Market(s)

Legal community; law firms; Big corporations requiring internal legal senior executive

Font styles to use
Serif

Colors
ffffff
85cae6
33a6d7
0292cd
86cfc6
cfeae6
757575
919191
d9d9d9

Requirements
Must have
• classy; serious; professional; elegant; easy to read; catchy; modern;

```html
<!DOCTYPE html>
<html lang="en">
<head>
<meta charset="utf-8">
<title>Curriculum Vitae – Experience</title>
<link href="https://fonts.googleapis.com/css2?family=Crimson+Text:wght@400;600&family=Open+Sans:wght@300;400&display=swap" rel="stylesheet">
<style>
  :root {
    --paper: #ffffff;
    --band: #cfeae6;
    --ink: #1f1f1f;
    --accent: #4f7c78;
    --muted: #757575;
    --rule: #b9b9b9;
  }
  * { margin: 0; padding: 0; box-sizing: border-box; }
  html, body { width: 848px; height: 1200px; overflow: hidden; background: var(--paper); }
  .page { position: relative; width: 848px; height: 1200px; background: var(--paper); font-family: "Crimson Text", Georgia, serif; color: var(--ink); }
  .section-band { position: absolute; left: 129px; top: 61px; width: 42px; height: 1096px; background: var(--band); }
  .section-label { position: absolute; left: 9px; top: 16px; writing-mode: vertical-rl; font-family: "Open Sans", Arial, sans-serif; font-weight: 300; font-size: 20px; letter-spacing: 1.5px; color: var(--accent); }
  .block { position: absolute; left: 300px; width: 487px; }
  .para { padding-left: 33px; font-size: 14.3px; line-height: 21.5px; text-align: justify; }
  .subhead { font-size: 18px; line-height: 22px; color: var(--accent); margin-bottom: 12px; }
  .duties { list-style: none; }
  .duties li { position: relative; padding-left: 33px; font-size: 14.3px; line-height: 21.5px; text-align: justify; margin-bottom: 12.3px; }
  .duties li::before { content: ""; position: absolute; left: 6px; top: 9px; width: 4px; height: 4px; border-radius: 50%; background: var(--ink); }
  .role-dates { position: absolute; left: 199px; top: 912px; width: 588px; padding-bottom: 4px; border-bottom: 1px solid var(--rule); font-family: "Open Sans", Arial, sans-serif; font-weight: 300; font-size: 18px; color: var(--muted); }
  .role-title { position: absolute; left: 239px; top: 950px; font-family: "Open Sans", Arial, sans-serif; font-weight: 300; font-size: 19.5px; line-height: 26px; color: var(--accent); }
</style>
</head>
<body>
<div class="page">
  <div class="section-band"><span class="section-label">EXPERIENCE</span></div>

  <p class="block para" style="top:76px;">Tender Documentation, Procurement Agreements, Mergers and Acquisitions, and other related to the development of company’s business in the Countries.</p>

  <div class="block" style="top:159px;">
    <h3 class="subhead">Digital:</h3>
    <ul class="duties">
      <li>Perform all the legal aspects of SHRL digital and ecommerce projects.</li>
      <li>Corporate Governance &amp; Compliance:</li>
      <li>Create and secure protection of Intellectual property.</li>
      <li>Ensure the application of SHRL corporate policies.</li>
      <li>Collaborate with the tax and finance groups to determine appropriate corporate structure.</li>
      <li>Communicate latest regulatory requirements to Business Units</li>
      <li>Develop and maintain legal processes and business transactions compliance and related training; Provide support for governmental relations and regulatory affairs activities.</li>
    </ul>
  </div>

  <div class="block" style="top:499px;">
    <h3 class="subhead">Risk Management</h3>
    <ul class="duties">
      <li>Lead the implementation of risk control measures, contractual obligations and the structuring of transactions.</li>
      <li>Pragmatically, manage legal risks and providing alternative solutions to minimize liability exposure while achieving business goals.</li>
    </ul>
  </div>

  <div class="block" style="top:649px;">
    <h3 class="subhead">Others</h3>
    <ul class="duties">
      <li>Review and negotiate (in conjunction with the Treasury department) of financial documentation required to satisfy the funding, banking and other monetary services’ requirements of the company;</li>
      <li>For new jurisdictions: Carry out legal research, due diligence procedures, prepare corporate documents and other formalities for the relevant operating companies. Establish methods to accomplish business goals whilst minimizing legal and commercial risks.</li>
      <li>Prepare board papers and updates to senior management</li>
    </ul>
  </div>

  <div class="role-dates">Nov 2011 - May 2015</div>
  <h2 class="role-title">Legal Counsel at Saif Hamdan Properties LLC<br>(“SHPL”) -Dubai</h2>

  <div class="block" style="top:1027px;">
    <h3 class="subhead">Description of Position:</h3>
    <p class="para">Lead and manage the Legal function related to the UAE shopping malls of SHPL in Dubai, Ajman, Sharjah, and Fujairah (Development, JVs, land acquisitions, asset management, leasing construction and project management).</p>
  </div>
</div>
</body>
</html>
```